Graphic Design Larkhollow Book Description

There is a book on Larkhollow that is my competitor that has a large graphic design as part of the description for the book and I want a similar thing for my book to make it stand out more.

My competitors book is here: https://www.larkhollow-books.example/Tidal-Chemistry-Starters-Grasping-Walkthrough/item/K47RZTX902/

My book is here: https://www.larkhollow-books.example/Tidal-Chemistry-Groundwork-Dynamics-Interlinking/item/K3P8WQE27T/

You can see the kind of thing I am looking for on the book listing but I have attached an image below.

Thanks

Owen

```html
<!DOCTYPE html>
<html lang="en">
<head>
<meta charset="UTF-8">
<title>Tidal Chemistry – Book Cover</title>
<link rel="stylesheet" href="https://fonts.googleapis.com/css2?family=Oswald:wght@500&family=Roboto+Condensed:wght@500&family=Roboto+Mono:wght@500&display=swap">
<style>
  :root {
    --page-bg: #1b2140;
    --cover-top: #0b1630;
    --cover-bottom: #0a1026;
    --ink-white: #ffffff;
    --ink-soft: #e8ecf6;
    --band-black: #050505;
    --glow-core: #4ea8ff;
    --glow-mid: #1a5fd0;
    --glow-edge: rgba(10, 20, 60, 0);
  }
  * { margin: 0; padding: 0; box-sizing: border-box; }
  html, body {
    width: 1200px;
    height: 1200px;
    overflow: hidden;
    background: var(--page-bg);
  }
  .canvas {
    position: relative;
    width: 1200px;
    height: 1200px;
  }
  .book-cover {
    position: absolute;
    left: 230px;
    top: 30px;
    width: 740px;
    height: 1140px;
    background: linear-gradient(180deg, var(--cover-top) 0%, var(--cover-bottom) 100%);
    color: var(--ink-white);
    text-align: center;
    overflow: hidden;
  }
  .cover-title {
    position: absolute;
    top: 46px;
    left: 0;
    width: 100%;
    font-family: "Oswald", sans-serif;
    font-weight: 500;
    font-size: 136px;
    line-height: 1.05;
    letter-spacing: 3px;
    text-transform: uppercase;
    white-space: nowrap;
  }
  .cover-subtitle {
    position: absolute;
    top: 368px;
    left: 40px;
    width: 660px;
    font-family: "Roboto Mono", monospace;
    font-weight: 500;
    font-size: 25px;
    line-height: 1.3;
    color: var(--ink-soft);
    text-transform: uppercase;
  }
  .cover-art {
    position: absolute;
    top: 470px;
    left: 140px;
    width: 460px;
    height: 420px;
  }
  .cover-band {
    position: absolute;
    top: 915px;
    left: 45px;
    width: 650px;
    height: 96px;
    background: var(--band-black);
    border-radius: 6px;
    display: flex;
    flex-direction: column;
    justify-content: center;
    font-family: "Roboto Condensed", sans-serif;
    font-weight: 500;
    font-size: 24px;
    line-height: 1.45;
    text-transform: uppercase;
    white-space: nowrap;
  }
  .cover-author {
    position: absolute;
    top: 1030px;
    left: 0;
    width: 100%;
    font-family: "Oswald", sans-serif;
    font-weight: 500;
    font-size: 68px;
    line-height: 1.2;
    letter-spacing: 3px;
    text-transform: uppercase;
  }
</style>
</head>
<body>
<main class="canvas">
  <section class="book-cover">
    <h1 class="cover-title">Tidal<br>Chemistry</h1>
    <p class="cover-subtitle">The Groundwork of Dynamics,<br>Interlinking and Current Theory</p>
    <svg class="cover-art" viewBox="0 0 460 420" role="img" aria-label="Glowing blue atom with orbiting electrons">
      <defs>
        <radialGradient id="atomGlow" cx="50%" cy="50%" r="50%">
          <stop offset="0%" stop-color="#4ea8ff"/>
          <stop offset="35%" stop-color="#1a5fd0" stop-opacity="0.75"/>
          <stop offset="100%" stop-color="#0a143c" stop-opacity="0"/>
        </radialGradient>
      </defs>
      <ellipse cx="230" cy="210" rx="230" ry="210" fill="url(#atomGlow)"/>
    </svg>
    <div class="cover-band">
      <span>A Starters Guide to Tidal Dynamics,</span>
      <span>Current Theory, Wave Theory, and Coastal Modelling</span>
    </div>
    <p class="cover-author">Elias Thornbury</p>
  </section>
</main>
</body>
</html>
```